Flyer Design - Halloween Dinner & Dance Function

We Need a Flyer Designed 'a la' Movie poster style
Vibrant Colours - Its for a Function on Halloween Weekend - but as opposed to traditional Halloween looking we want it very much slick modern in the style of 'The Ember Chronicles' Mood and Settings especially the Fonts – with Respect No Old Skool 'Morvane Type' Fonts please.

Please see attached document for specific type examples.

We need the flyer to work as a Landscape A5 Flyer and also as a 5cm High by 15cm wide strip Flyer

We need it in both Jpeg and PDF Files & Chosen Design without Text in Both Formats.

As the project is needed for this Halloween - Time and Speed are of the essence if possible please ! and we need to see Mock Ups asap, - We need/ would like to choose a design/ designer by Tuesday 12th Oct 2010 Please Thank You

Thank You.

Movie

• - The Pics should be head shots ONLY please like the examples that have been provided - Thank You
• Also The Main Act is the Prominent Name.

```html
<!DOCTYPE html>
<html lang="en">
<head>
<meta charset="utf-8">
<title>Soul on Halloween – Strip Flyer</title>
<link rel="stylesheet" href="https://fonts.googleapis.com/css2?family=Bebas+Neue&family=Cinzel:wght@400;600&display=swap">
<style>
  :root {
    --page: #ffffff;
    --night: #0d0b12;
    --storm: #3b3550;
    --cloud: #a9a3c4;
    --cloud-light: #d6d2e8;
    --moon: #b9b7bd;
    --moon-dark: #6d6b72;
    --text: #f4f2f8;
    --text-shadow: #1a1622;
  }
  * { margin: 0; padding: 0; box-sizing: border-box; }
  html, body { width: 1200px; height: 900px; overflow: hidden; background: var(--page); }
  .flyer {
    position: absolute; left: 100px; top: 265px; width: 1000px; height: 333px;
    overflow: hidden;
    background:
      radial-gradient(ellipse 260px 120px at 560px 200px, var(--cloud) 0%, rgba(169,163,196,0) 100%),
      radial-gradient(ellipse 340px 140px at 760px 230px, var(--cloud-light) 0%, rgba(214,210,232,0) 100%),
      radial-gradient(ellipse 420px 260px at 480px 60px, var(--storm) 0%, rgba(59,53,80,0) 100%),
      linear-gradient(90deg, var(--night) 0%, #231f30 40%, #4a4463 65%, #2a2638 88%, var(--night) 100%);
    font-family: 'Bebas Neue', sans-serif;
    color: var(--text);
  }
  .moon {
    position: absolute; left: 565px; top: -55px; width: 380px; height: 380px; border-radius: 50%;
    background: radial-gradient(circle at 45% 45%, var(--moon) 0%, #9d9ba2 55%, var(--moon-dark) 85%, rgba(109,107,114,0) 100%);
    opacity: .85;
  }
  .branches {
    position: absolute; left: 620px; top: 215px; width: 380px; height: 118px;
    background: radial-gradient(ellipse 200px 60px at 50% 100%, rgba(13,11,18,.85) 0%, rgba(13,11,18,0) 100%);
  }
  .headshot { position: absolute; }
  .headshot--glen { left: 40px; top: 55px; width: 140px; height: 190px;
    background: radial-gradient(ellipse 50% 50% at 50% 45%, #8a5a44 0%, #6b4434 45%, rgba(42,32,40,.6) 80%, rgba(42,32,40,0) 100%); }
  .headshot--rj { left: 160px; top: 20px; width: 160px; height: 260px;
    background: radial-gradient(ellipse 50% 50% at 50% 40%, #7a4a36 0%, #4a2c22 40%, rgba(21,18,26,.8) 75%, rgba(21,18,26,0) 100%); }
  .headshot--nina { left: 305px; top: 60px; width: 135px; height: 200px;
    background: radial-gradient(ellipse 50% 50% at 50% 42%, #d6a893 0%, #8a5a4a 40%, rgba(42,28,28,.7) 75%, rgba(42,28,28,0) 100%); }
  .line { position: absolute; white-space: nowrap; letter-spacing: 1px; text-shadow: 0 0 2px var(--text-shadow); }
  .act-name { font-size: 17px; }
  .act-sub { font-size: 11px; letter-spacing: 1.2px; }
  .title { position: absolute; font-family: 'Cinzel', serif; font-weight: 600; color: var(--text);
    -webkit-text-stroke: 1px var(--text-shadow); text-shadow: 2px 2px 3px rgba(0,0,0,.6); line-height: 1; }
  .title--soul { left: 685px; top: 18px; font-size: 48px; }
  .title--on { left: 733px; top: 62px; font-size: 14px; }
  .title--halloween { left: 565px; top: 73px; font-size: 55px; letter-spacing: 1px; }
  .event { position: absolute; left: 560px; width: 405px; text-align: center; font-size: 21px; line-height: 21px; letter-spacing: 1.5px; text-shadow: 1px 1px 2px var(--text-shadow); }
  .tickets { position: absolute; left: 560px; top: 243px; width: 405px; text-align: center; font-size: 10px; line-height: 16px; letter-spacing: 1px; }
</style>
</head>
<body>
  <section class="flyer">
    <div class="moon" role="img" aria-label="Full moon rising over storm clouds"></div>
    <div class="branches" role="img" aria-label="Silhouetted bare tree branches"></div>

    <div class="headshot headshot--glen" role="img" aria-label="Head shot of Glen Ashford"></div>
    <div class="headshot headshot--rj" role="img" aria-label="Head shot of RJ Calloway, the main act"></div>
    <div class="headshot headshot--nina" role="img" aria-label="Head shot of Nina Castell"></div>

    <p class="line act-name" style="left:53px;top:38px;">Glen Ashford</p>
    <p class="line act-sub" style="left:291px;top:7px;">Plus special 'Carol Dearing' show by</p>
    <p class="line act-name" style="left:338px;top:24px;">Nina Castell</p>
    <p class="line act-name" style="left:133px;top:266px;font-size:18px;">RJ 'Mr Soul Engine' Calloway</p>
    <p class="line act-sub" style="left:145px;top:288px;">Singing the hits of 80's soul &amp; Rivertown</p>

    <h1>
      <span class="title title--soul">SOUL</span>
      <span class="title title--on">ON</span>
      <span class="title title--halloween">HALLOWEEN</span>
    </h1>

    <p class="event" style="top:155px;">At The Quayhouse (Harlow Bay)</p>
    <p class="event" style="top:175px;">Friday 29th October, 7pm-Midnight</p>
    <p class="event" style="top:197px;">Special Guest! Club &amp; Soul DJ Legend!!</p>

    <div class="tickets">
      <p>Lounge/Bar &amp; Show Tickets £12.50</p>
      <p>Lounge/Bar &amp; Show tickets can only be purchased from these numbers</p>
      <p>Dee: 07700 900123 &nbsp; Rafe: 07700 900456</p>
      <p>For table/dinner reservations call: 01632 960588</p>
    </div>
  </section>
</body>
</html>
```